UK Glass Restoration Company needs a Direct Mail Postcard Design

We need a HARD HITTING, COMPELLING 300dpi Camera Ready double sided postcard.
The dimensions will be 109mm x 152mm including bleed. We are a scratched glass repair / etched graffiti removal glass restoration company based in London, UK.
We operate mainly within the construction and commercial marketplace, however this particular postcard design is aimed solely at shop owners who have become victims of vandalism, due to etched graffiti tags and or scratches being left on their shop front glass.
We wish to focus the shop / business owners mind to the negative impact such vandalism has on the image of their business and how we are able to offer a quick and cost effective solution
We will supply text for both sides of the postcard along with relevant images, company logo and previous flyer designs, however we are happy for the selected designer to source suitable alternative images provided they are in keeping with the exact "Before" and "After" theme.
The finished postcard must preferably have a white background, but again we are open to creative suggestions.
Target Market(s)
UK SHOP OWNERS
Industry/Entity Type
It Company

```html
<!DOCTYPE html>
<html lang="en">
<head>
<meta charset="utf-8">
<title>Lucent Glass Repairs – Postcard Front</title>
<link rel="stylesheet" href="https://fonts.googleapis.com/css2?family=Fira+Sans+Extra+Condensed:wght@600;700&family=Roboto+Condensed:wght@400;500;600&display=swap">
<style>
  :root {
    --paper: #ffffff;
    --ink: #111111;
    --band: #070912;
    --headline: #f2f2f4;
    --accent: #f5e800;
    --body-text: #ffffff;
    --brand-blue: #27a7e6;
    --glass-top: #b9c0cd;
    --glass-mid: #7d83a8;
    --glass-low: #5a5a8a;
  }
  * { margin: 0; padding: 0; box-sizing: border-box; }
  html, body { width: 880px; height: 1200px; overflow: hidden; background: var(--paper); }
  .sheet { position: relative; width: 880px; height: 1200px; background: var(--paper); }
  .side-label {
    position: absolute; top: 28px; left: 0; width: 880px; text-align: center;
    font: 700 26px "Fira Sans Extra Condensed", sans-serif; color: var(--ink);
  }
  .crop-marks { position: absolute; inset: 0; }
  .postcard {
    position: absolute; left: 53px; top: 72px; width: 772px; height: 1056px;
    background: var(--band); overflow: hidden;
  }
  .band { position: absolute; left: 0; width: 100%; background: var(--band); }
  .band-top { top: 0; height: 123px; }
  .band-bottom { top: 868px; height: 188px; }
  .glass-photo {
    position: absolute; left: 0; top: 123px; width: 100%; height: 745px;
    background: linear-gradient(180deg, var(--glass-top) 0%, #c9cdd8 8%, #8c90b0 20%, var(--glass-mid) 45%, var(--glass-low) 100%);
  }
  .brand-box {
    position: absolute; left: 467px; top: 50px; width: 234px; height: 110px;
    background: var(--ink); padding: 11px 6px;
  }
  .brand-box-inner {
    width: 100%; height: 100%; background: var(--paper);
    display: flex; align-items: center; justify-content: center; gap: 7px;
  }
  .brand-dot { width: 10px; height: 10px; border-radius: 50%; background: var(--brand-blue); flex: none; }
  .brand-name {
    font: 500 21px "Roboto Condensed", sans-serif; color: var(--brand-blue);
    line-height: 1; white-space: nowrap;
  }
  .headline {
    position: absolute; left: 0; top: 0; width: 100%;
    font-family: "Fira Sans Extra Condensed", sans-serif; font-weight: 600;
    color: var(--headline); text-transform: uppercase; line-height: 1;
    text-shadow: 0 2px 3px rgba(0,0,0,.35);
  }
  .headline span { position: absolute; white-space: nowrap; }
  .h-before { left: 124px; top: 160px; font-size: 66px; }
  .h-repair { left: 156px; top: 222px; font-size: 128px; }
  .h-bad { left: 122px; top: 342px; font-size: 68px; }
  .h-first { left: 169px; top: 402px; font-size: 68px; }
  .h-impression { left: 66px; top: 460px; font-size: 92px; }
  .tagline {
    position: absolute; left: 67px; top: 580px;
    font: 600 37px "Fira Sans Extra Condensed", sans-serif; color: var(--accent);
    text-shadow: 0 2px 3px rgba(0,0,0,.4); white-space: nowrap;
  }
  .intro {
    position: absolute; left: 69px; top: 627px; width: 668px;
    font: 500 17.5px/21.5px "Roboto Condensed", sans-serif; color: var(--body-text);
    text-align: justify; text-shadow: 0 1px 2px rgba(0,0,0,.6);
  }
  .divider {
    position: absolute; left: 67px; top: 820px; width: 670px; border-top: 2px dashed var(--paper);
  }
  .cta-label {
    position: absolute; left: 67px; top: 842px;
    font: 600 27px "Fira Sans Extra Condensed", sans-serif; color: var(--accent);
  }
  .cta-phone {
    position: absolute; left: 67px; top: 875px;
    font: 600 28px "Roboto Condensed", sans-serif; color: var(--body-text);
  }
  .cta-web {
    position: absolute; left: 67px; top: 910px;
    font: 400 22px "Roboto Condensed", sans-serif; color: var(--body-text);
  }
</style>
</head>
<body>
<div class="sheet">
  <div class="side-label">FRONT</div>
  <svg class="crop-marks" width="880" height="1200" viewBox="0 0 880 1200" aria-hidden="true">
    <g stroke="#111" stroke-width="1.2">
      <line x1="80" y1="46" x2="80" y2="72"/><line x1="798" y1="46" x2="798" y2="72"/>
      <line x1="27" y1="99" x2="53" y2="99"/><line x1="825" y1="99" x2="851" y2="99"/>
      <line x1="27" y1="1101" x2="53" y2="1101"/><line x1="825" y1="1101" x2="851" y2="1101"/>
      <line x1="80" y1="1128" x2="80" y2="1154"/><line x1="798" y1="1128" x2="798" y2="1154"/>
    </g>
  </svg>
  <div class="postcard">
    <div class="band band-top"></div>
    <div class="glass-photo" role="img" aria-label="Close-up photo of a shop window pane covered in etched scratches and graffiti marks"></div>
    <div class="band band-bottom"></div>
    <div class="brand-box">
      <div class="brand-box-inner">
        <span class="brand-dot"></span>
        <span class="brand-name">Lucent Glass Repairs</span>
      </div>
    </div>
    <h1 class="headline">
      <span class="h-before">Before</span>
      <span class="h-repair">Repair –</span>
      <span class="h-bad">A Bad</span>
      <span class="h-first">First</span>
      <span class="h-impression">Impression</span>
    </h1>
    <p class="tagline">Don't Let Vandals Wreck Your Image!</p>
    <p class="intro">What's on display in your shop window? If it's graffiti, vandalism, or just wear and tear, that's the first impression your customers get – and it's not good. Lucent Glass Repairs remove damage from glass windows, making them sparkling clear – without replacing the glass! Our glass repair work is effective, green, and very economical. See our coupon on the other side to save even more!</p>
    <div class="divider"></div>
    <p class="cta-label">Call Now For Expert Advice :</p>
    <p class="cta-phone">0800 555 0147</p>
    <p class="cta-web">www.lucentglassrepairs.co.uk</p>
  </div>
</div>
</body>
</html>
```